Book cover for book about Climate Change

Looking for a clean, bold, and attractive cover for a mass-market paperback (5.5"x 8.5") about solving the climate change problem. Title is either "When Rivers Learn to Sing” or A Lantern Over Quiet Fields” (your choice), subtitle is "A five-step plan to reverse climate change — to ensure that your grandchildren will live on a clean and comfortable planet," author is Dale Pruitt. Thinking that it *might* feature an image of Earth (or a portion thereof) and its very thin layer of atmosphere -- but STRONGLY encourage other ideas too!

Requirements
Nice to have
• Keep it positive — NOT scary doom-and-gloom

```html
<!DOCTYPE html>
<html lang="en">
<head>
<meta charset="utf-8">
<title>A Lantern Over Quiet Fields – Cover Spread</title>
<link href="https://fonts.googleapis.com/css2?family=Oswald:wght@200;300;600&family=Montserrat:wght@400;600&display=swap" rel="stylesheet">
<style>
  :root {
    --backdrop: #aedff9;
    --cover-deep: #1c4a80;
    --cover-mid: #245d98;
    --cover-light: #3a82b6;
    --spine: #1d4b82;
    --title-white: #ffffff;
    --accent-blue: #5cb0e2;
    --rule-blue: #4fa3d8;
    --body-white: #f2f7fc;
  }
  * { margin: 0; padding: 0; box-sizing: border-box; }
  html, body {
    width: 1200px; height: 900px; overflow: hidden;
    background: var(--backdrop);
  }
  .spread {
    position: absolute; left: 150px; top: 119px;
    width: 902px; height: 662px;
    font-family: "Montserrat", sans-serif;
    color: var(--body-white);
  }
  .back-cover {
    position: absolute; left: 0; top: 0; width: 429px; height: 662px;
    background: linear-gradient(160deg, var(--cover-light) 0%, var(--cover-mid) 40%, var(--cover-deep) 75%, var(--cover-light) 100%);
  }
  .spine {
    position: absolute; left: 429px; top: 0; width: 45px; height: 662px;
    background: var(--spine);
  }
  .front-cover {
    position: absolute; left: 474px; top: 0; width: 428px; height: 662px;
    background: radial-gradient(circle at 68% 50%, #3a8cc6 0%, var(--cover-mid) 45%, var(--cover-deep) 100%);
    overflow: hidden;
  }
  .rule { position: absolute; background: var(--rule-blue); opacity: .75; }
  .rule.h { height: 1px; }
  .rule.v { width: 1px; }

  .title { font-family: "Oswald", sans-serif; text-transform: uppercase; white-space: nowrap; }
  .title span { display: block; }
  .title .thin { font-weight: 200; color: var(--title-white); }
  .title .bold { font-weight: 600; color: var(--accent-blue); }

  /* back */
  .back-title { position: absolute; left: 25px; top: 18px; font-size: 38px; line-height: 32px; letter-spacing: -0.5px; }
  .back-title .bold { font-size: 44px; line-height: 38px; }
  .back-author { position: absolute; left: 25px; top: 200px; font-size: 11px; }
  .blurb { position: absolute; left: 170px; top: 250px; width: 225px; font-size: 11px; line-height: 13px; }
  .blurb p { margin-bottom: 13.5px; }

  /* spine */
  .spine-text {
    position: absolute; left: 6px; writing-mode: vertical-rl;
    white-space: nowrap;
  }
  .spine-title { top: 128px; font-size: 27px; line-height: 32px; letter-spacing: -0.3px; }
  .spine-title .thin, .spine-title .bold { display: inline; }
  .spine-author { top: 513px; left: 12px; font-size: 19px; color: var(--title-white); }

  /* front */
  .globe {
    position: absolute; left: 175px; top: 215px; width: 222px; height: 222px;
    border-radius: 50%;
    background: radial-gradient(circle at 40% 35%, #8fae84 0%, #4d7d78 35%, #2f6aa0 65%, #163e6e 100%);
    box-shadow: 0 0 30px 8px rgba(150, 210, 250, .55);
  }
  .front-title { position: absolute; left: 46px; top: 77px; letter-spacing: -1px; }
  .front-title .thin { font-size: 88px; line-height: 87px; }
  .front-title .bold { font-size: 100px; line-height: 100px; opacity: .92; }
  .tagline {
    position: absolute; left: 190px; top: 65px; width: 150px;
    font-size: 10.5px; line-height: 13px; color: var(--title-white);
  }
  .tagline b { font-weight: 600; }
  .front-author {
    position: absolute; right: 92px; top: 561px;
    font-size: 19.5px; color: var(--title-white); white-space: nowrap;
  }
</style>
</head>
<body>
<div class="spread">

  <section class="back-cover">
    <h2 class="title back-title">
      <span class="thin">A</span>
      <span class="thin">Lantern</span>
      <span class="thin">Over</span>
      <span class="bold">Quiet</span>
      <span class="bold">Fields</span>
    </h2>
    <p class="back-author">Dale Pruitt</p>
    <div class="rule v" style="left:154px; top:120px; height:130px;"></div>
    <div class="rule h" style="left:43px; top:234px; width:111px;"></div>
    <div class="blurb">
      <p>Lorem ipsum dolor sit amet, consectetur adipiscing elit, sed do eiusmod tempor incididunt ut labore et dolore magna aliqua. Quis ipsum suspendisse ultrices gravida. Risus commodo viverra maecenas accumsan lacus vel facilisis.</p>
      <p>Lorem ipsum dolor sit amet, consectetur adipiscing elit, sed do eiusmod tempor incididunt ut labore et dolore magna aliqua. Quis ipsum suspendisse ultrices gravida. Risus commodo viverra maecenas accumsan lacus vel facilisis.</p>
      <p>Lorem ipsum dolor sit amet, consectetur adipiscing elit, sed do eiusmod tempor incididunt ut labore et dolore magna aliqua. Quis ipsum suspendisse ultrices gravida. Risus commodo viverra maecenas accumsan lacus vel facilisis.</p>
    </div>
  </section>

  <section class="spine">
    <p class="title spine-text spine-title"><span class="thin">A Lantern Over </span><span class="bold">Quiet Fields</span></p>
    <p class="spine-text spine-author">Dale Pruitt</p>
  </section>

  <section class="front-cover">
    <div class="rule v" style="left:172px; top:25px; height:125px;"></div>
    <div class="rule h" style="left:172px; top:150px; width:160px;"></div>
    <p class="tagline">A <b>five-step plan</b> to reverse climate change — to ensure that your grandchildren will live on <b>a clean and comfortable planet</b></p>

    <div class="globe" role="img" aria-label="Photograph of planet Earth with its thin glowing atmosphere"></div>

    <h1 class="title front-title">
      <span class="thin">A</span>
      <span class="thin">Lantern</span>
      <span class="thin">Over</span>
      <span class="bold">Quiet</span>
      <span class="bold">Fields</span>
    </h1>

    <div class="rule h" style="left:92px; top:560px; width:336px;"></div>
    <div class="rule h" style="left:214px; top:593px; width:214px;"></div>
    <div class="rule v" style="left:361px; top:467px; height:144px;"></div>
    <p class="front-author">Dale Pruitt</p>
  </section>

</div>
</body>
</html>
```